CuraNex System Web Page Design

This project is to design 6 pages of a web based medical system for clinics, hospitals, drugs suppliers, general items suppliers, insurance company, laboratories and patients (basically all parties which could be involved in).We want the designs of the browser, button, icon and layout are based on Vex, which is user friendly, looks professional, simple and neat but with powerful functions. We have uploaded few pictures of another system, please do not copy its design because this is not what we are looking for, the pictures are for you to know the elements should be included in our pages. CuraNex web-base system, design 6 pages1. Login PageShould include the following elements-company id with input field-login id with input field-password with input field2. Main Page (Navigation page)Should include the following elements-Appointment-Consultation-Patient-Drugs inventory -General supplies inventory -Laboratory-Suppliers-Insurance-Reports 3. Appointment PageShould include all the the elements in the respective pictures plus the followings-Daily View, Weekly View, Monthly View buttons4. Consultation PageShould include all the the elements in the respective picture5. Patient Page5.1 General information Should include all the the elements in the respective picture5.2 medical history/lab reportsShould include all the the elements in the respective picture plus the followings-Notify patient button-Share report button.
Updated on 28 Nov:
Please stop using Ward Keystone in your designs which is not the name of our system. We have just rename our system to CuraNex, please take note.
We need the system to look professional not playful, do not use too many colors and playful icons.
professional users

```html
<!DOCTYPE html>
<html lang="en">
<head>
<meta charset="utf-8">
<title>Medora Clinic – Search Results</title>
<link href="https://fonts.googleapis.com/css2?family=Raleway:wght@400;500;600&display=swap" rel="stylesheet">
<style>
  :root{
    --board:#3768f0;
    --brand:#3a66e8;
    --white:#ffffff;
    --chrome:#f9f8f6;
    --ink:#333a44;
    --muted:#6b7079;
    --line:#3a66e8;
    --dot-red:#e0100f;
    --dot-yellow:#f1c40f;
    --dot-green:#6fdc2b;
  }
  *{box-sizing:border-box;margin:0;padding:0}
  html,body{width:1200px;height:675px;overflow:hidden}
  body{background:var(--board);font-family:"Raleway",sans-serif;color:var(--ink);position:relative}
  .board-title{position:absolute;top:18px;left:0;width:1200px;text-align:center;color:var(--white);font-size:19px;font-weight:500}
  .notes{position:absolute;left:914px;top:98px;width:260px;color:var(--white)}
  .notes h2{font-size:20px;font-weight:500;margin-left:4px;margin-bottom:40px}
  .notes p{font-size:15.4px;line-height:18.2px;font-weight:400}

  .window{position:absolute;left:87.5px;top:98px;width:800px;height:478px;background:var(--white);overflow:hidden}
  .chrome{height:28px;background:var(--chrome);position:relative}
  .chrome span{position:absolute;top:8px;width:12px;height:12px;border-radius:50%}
  .chrome .red{left:16px;background:var(--dot-red)}
  .chrome .yellow{left:38px;background:var(--dot-yellow)}
  .chrome .green{left:60px;background:var(--dot-green)}
  .app-header{height:30px;position:relative;box-shadow:0 2px 4px rgba(0,0,0,.05)}
  .app-name{position:absolute;left:33px;top:6px;font-size:13px;font-weight:500;color:var(--brand)}
  .lang{position:absolute;left:650px;top:9px;font-size:7px;color:var(--brand);display:flex;align-items:center;gap:3px}
  .avatar{position:absolute;left:683px;top:5px;width:19px;height:19px;border-radius:50%;background:linear-gradient(135deg,#c9a48c,#4a4e57)}
  .user{position:absolute;left:706px;top:9px;font-size:8.5px;color:var(--brand);display:flex;align-items:center;gap:6px}

  .abs{position:absolute}
  .back{left:36px;top:71px}
  .page-title{left:95px;top:71px;font-size:10.6px;color:var(--brand)}
  .search{left:218px;top:87.5px;width:364px;height:21px;border:1px solid var(--line);display:flex;align-items:center;padding-left:6px;gap:5px;font-size:8px;color:var(--muted)}
  .btn{background:var(--brand);color:var(--white);font-size:6.5px;font-weight:600;display:flex;align-items:center;justify-content:center;box-shadow:0 2px 4px rgba(0,0,0,.18)}
  .btn-new{left:626px;top:87.5px;width:79px;height:21px}
  .match{left:156px;top:121px;font-size:6.3px;color:var(--muted)}
  .result-card{left:161px;top:138px;width:479px;height:132px;background:var(--white);box-shadow:0 2px 8px rgba(0,0,0,.16)}
  .field{position:absolute;font-size:5.8px}
  .field .label{color:var(--brand);display:block}
  .field .value{color:var(--ink);display:block;margin-top:4.5px}
  .btn-profile{left:362.5px;top:240px;width:75px;height:21px}
  .btn-all{left:362.5px;top:377.5px;width:75px;height:21px}
</style>
</head>
<body>
  <h1 class="board-title">Medora Clinic</h1>

  <main class="window">
    <div class="chrome"><span class="red"></span><span class="yellow"></span><span class="green"></span></div>
    <header class="app-header">
      <div class="app-name">Medora Clinic.</div>
      <div class="lang">
        <svg width="8" height="8" viewBox="0 0 10 10" fill="none" stroke="#3a66e8" stroke-width="1"><circle cx="5" cy="5" r="4.2"/><ellipse cx="5" cy="5" rx="1.8" ry="4.2"/><path d="M0.8 5h8.4"/></svg>EN
      </div>
      <div class="avatar" role="img" aria-label="User profile photo"></div>
      <div class="user">Omar Lindqvist
        <svg width="6" height="4" viewBox="0 0 6 4" fill="none" stroke="#3a66e8" stroke-width="1"><path d="M0.5 0.5l2.5 2.5 2.5-2.5"/></svg>
      </div>
    </header>

    <svg class="abs back" width="17" height="10" viewBox="0 0 17 10" fill="none" stroke="#3a66e8" stroke-width="1.5"><path d="M16 5H1.5M5.5 1L1.5 5l4 4"/></svg>
    <div class="abs page-title">Appointments</div>

    <div class="abs search">
      <svg width="9" height="9" viewBox="0 0 10 10" fill="none" stroke="#6b7079" stroke-width="0.9"><circle cx="6" cy="4" r="3.2"/><path d="M3.7 6.3L0.8 9.2"/></svg>
      Daniel Hart
    </div>
    <div class="abs btn btn-new">NEW APPOINTMENT</div>

    <div class="abs match">1 Match found</div>

    <section class="abs result-card">
      <div class="field" style="left:34px;top:7px"><span class="label">Patient Code</span><span class="value">&nbsp;00123</span></div>
      <div class="field" style="left:180px;top:7px"><span class="label">Birth date</span><span class="value">&nbsp;22 - Jan - 1990</span></div>
      <div class="field" style="left:326px;top:7px"><span class="label">Doctor</span><span class="value">&nbsp;Dr. Ruth Okafor</span></div>
      <div class="field" style="left:34px;top:37px"><span class="label">Full Name</span><span class="value">Daniel Hart</span></div>
      <div class="field" style="left:180px;top:37px"><span class="label">App. Date and Time</span><span class="value">12:00 PM on 13 - Nov - 2018</span></div>
      <div class="field" style="left:326px;top:37px"><span class="label">Remarks</span><span class="value">-</span></div>
      <div class="field" style="left:34px;top:67px"><span class="label">Gender</span><span class="value">Male</span></div>
      <div class="field" style="left:180px;top:67px"><span class="label">Clinic</span><span class="value">Brightwell Clinic</span></div>
      <div class="field" style="left:326px;top:66px"><span class="label">Duration</span><span class="value">-</span></div>
    </section>
    <div class="abs btn btn-profile">VIEW PROFILE</div>

    <div class="abs btn btn-all">VIEW ALL</div>
  </main>

  <aside class="notes">
    <h2>Search Results</h2>
    <p>This screen shows the search results. The user can see the details of patient with option to view complete profile and option to go back to ‘View All’ patients.</p>
  </aside>
</body>
</html>
```